依頼詳細
会社の名刺デザインを新しくします。
中核になる3つの事業にそれぞれスタッフがいますが、名刺は共通のものを使用したいと考えています。
スタイリッシュかつ遊び心があって、もらった人が目を引くような名刺にしたいです。
あえてカラーなど希望イメージの指定は致しませんので、多種多様のデザインを見て決めたいと思います。
会社ロゴを添付します。カラーは自由に変更していただいて構いません。
記載項目
表面:社名、事業名、肩書き、名前、連絡先(住所、TEL、FAX、メール等)
裏面:事業内容、プロフィールなど
希望イメージ
シンプル 複雑
単色 カラフル
暗い 明るい
日常 高級
遊び心 厳粛
未来的 伝統的
女性的 男性的
希望する色
設定なし
納品ファイル
設定なし
補足説明
設定なし
縦型、横型、二つ折り名刺、顔写真入りなども特に定めませんので、自由にご提案いただけると選びがいがあり有り難いです。
当選報酬の金額引き上げと選定確約について変更致しました。
よろしくお願い致します。
会社ロゴを添付しました。
ランサーの皆様、たくさんの提案ありがとうございます。
様々な提案を見た結果イメージが固まってきましたので、締め切りを延長して修正等をしていただけないかと思います。

【追記内容】
・事業所名が和風なので、和風な感じが合いそう。
・事業所名の「楓庵の里」は筆文字にしたらいいのではないか?
・匠な感じが出るといい。(白と黒を基調にするとどうなるでしょう?他の色でも構えいません。)
■ 選んだ理由

社員全員による投票にて決定いたしましたので、万人受けしやすいデザインだったのではないかと思います。また、修正等に幾度も迅速に対応していただいた点もよかったです。

■ 提案者全員のお礼・コメント

70を超すランサーの方々から100を超える提案を頂き誠にありがとうございました。当選作品以外にも素晴らしいデザインが多く、選定するのも大変でした。ありがとうございました。

```html
<!DOCTYPE html>
<html lang="ja">
<head>
<meta charset="utf-8">
<title>ケアテクト 名刺デザイン</title>
<link href="https://fonts.googleapis.com/css2?family=Shippori+Mincho:wght@500;700&family=Noto+Sans+JP:wght@400;700&family=Yuji+Syuku&display=swap" rel="stylesheet">
<style>
:root{
  --board:#c9c9c9;
  --label:#f4f4f4;
  --paper:#ecebe8;
  --paper-dark:#e2e0dc;
  --white:#ffffff;
  --rose:#d9506a;
  --rose-soft:#f2c9d0;
  --pink-tri:#f6d1d8;
  --red:#c8283a;
  --ink:#3a3a3a;
  --grey:#6c6c6c;
  --sky:#bfe0ef;
  --sky-ink:#2e8fbf;
  --butter:#f7e6a0;
  --butter-ink:#a08416;
}
*{margin:0;padding:0;box-sizing:border-box}
html,body{width:809px;height:1200px;overflow:hidden;background:var(--board)}
body{position:relative;font-family:"Noto Sans JP",sans-serif;color:var(--ink)}
.side-label{position:absolute;left:60px;font-size:20px;color:var(--label)}
.card{position:absolute;left:113px;width:615px;height:372px;overflow:hidden;box-shadow:0 4px 10px rgba(0,0,0,.25);background:var(--white)}
.card--front{top:160px}
.card--back{top:598px}

/* front */
.front-upper{position:absolute;left:0;top:0;width:100%;height:190px;background:linear-gradient(135deg,var(--paper),var(--paper-dark))}
.brand{position:absolute;left:22px;top:18px;width:90px;text-align:center}
.brand-mark{width:72px;height:72px;border-radius:50%;background:var(--rose);margin:0 auto 6px}
.brand-name{font-family:"Shippori Mincho",serif;font-weight:700;color:var(--rose);font-size:14px}
.role{position:absolute;left:235px;top:62px;font-family:"Shippori Mincho",serif;font-size:14px}
.person{position:absolute;left:230px;top:86px;font-family:"Shippori Mincho",serif;font-weight:700;font-size:34px;letter-spacing:6px;white-space:nowrap}
.person small{font-family:"Noto Sans JP",sans-serif;font-weight:400;font-size:10px;letter-spacing:0;margin-left:8px;color:var(--grey)}
.rule{position:absolute;left:230px;right:24px;top:134px;height:1px;background:#b9b6b1}
.motto{position:absolute;left:0;right:0;top:140px;height:30px;line-height:30px;padding-left:232px;font-family:"Shippori Mincho",serif;font-weight:700;color:var(--red);font-size:13px;white-space:nowrap;background:rgba(255,255,255,.45)}
.company{position:absolute;left:22px;top:198px;font-family:"Shippori Mincho",serif;font-weight:700;font-size:18px}
.contact{position:absolute;left:22px;top:228px;list-style:none;font-size:12px;line-height:24px;color:var(--grey)}
.contact li{display:flex;align-items:center;gap:6px}
.contact svg{width:12px;height:12px;fill:var(--grey)}
.front-accent{position:absolute;right:-40px;bottom:-50px;width:220px;height:220px;border-radius:50%;background:var(--rose-soft);opacity:.45}

/* back */
.back-rail{position:absolute;left:0;top:0;width:120px;height:100%;background:var(--white)}
.back-rail .brand{left:15px;top:14px}
.tagline-vertical{position:absolute;left:44px;top:128px;height:232px;writing-mode:vertical-rl;transform:rotate(180deg);text-align:center;font-family:"Shippori Mincho",serif;font-weight:700;color:var(--red);font-size:17px;line-height:1;white-space:nowrap}
.back-field{position:absolute;left:120px;top:0;right:0;bottom:0;background:linear-gradient(135deg,var(--paper),var(--paper-dark))}
.arc{position:absolute;left:0;top:0;width:100%;height:100%}
.place{position:absolute;left:20px;top:16px;font-family:"Yuji Syuku",serif;font-weight:400;color:var(--red);font-size:50px;line-height:1}
.slogan{position:absolute;left:235px;top:14px;font-family:"Shippori Mincho",serif;color:var(--red);font-size:13px;white-space:nowrap}
.phone-box{position:absolute;left:232px;top:36px;width:255px;height:32px;background:var(--rose);color:var(--white);font-weight:700;font-size:19px;line-height:32px;padding-left:10px}
.service{position:absolute;isolation:isolate;text-align:center;font-family:"Shippori Mincho",serif;font-weight:700;font-size:13px;line-height:1.35;color:var(--ink)}
.service-shape{position:absolute;left:0;top:0;z-index:0}
.service-text{position:relative;z-index:1}
.service-title{font-family:"Noto Sans JP",sans-serif;font-size:13px}
.service--nursing{left:40px;top:84px;width:160px;height:136px}
.service--nursing .service-text{padding-top:42px}
.service--nursing .service-title{color:var(--red)}
.service--day{left:300px;top:90px;width:150px;height:128px}
.service--day .service-text{padding-top:60px}
.service--day .service-title{color:var(--sky-ink)}
.service--care{left:150px;top:212px;width:200px;height:150px}
.service--care .service-text{padding-top:58px}
.service--care .service-title{color:var(--butter-ink)}
</style>
</head>
<body>
<div class="side-label" style="top:96px">Front</div>
<section class="card card--front">
  <div class="front-upper"></div>
  <div class="front-accent"></div>
  <div class="brand"><div class="brand-mark"></div><div class="brand-name">care tecto</div></div>
  <p class="role">代表取締役</p>
  <p class="person">山田 太郎<small>Taro Yamada</small></p>
  <div class="rule"></div>
  <p class="motto">自立支援のプロとして地域に必要不可欠な存在を目指す。</p>
  <p class="company">株式会社ケアテクト</p>
  <ul class="contact">
    <li><svg viewBox="0 0 12 12"><path d="M6 0a4 4 0 0 0-4 4c0 3 4 8 4 8s4-5 4-8a4 4 0 0 0-4-4zm0 5.5A1.5 1.5 0 1 1 6 2.5a1.5 1.5 0 0 1 0 3z"/></svg>〒123-4567 〇〇〇〇〇〇〇〇〇〇〇〇〇〇</li>
    <li><svg viewBox="0 0 12 12"><path d="M2.5 0l2 3-1.2 1.3a7 7 0 0 0 4.4 4.4L9 7.5l3 2-1.5 2.5C5 12 0 7 0 1.5z"/></svg>Tel: 0000-00-0000 <svg viewBox="0 0 12 12"><rect x="1" y="3" width="10" height="7"/><rect x="3" y="0" width="6" height="3"/></svg>Fax. 0000-00-0000</li>
    <li><svg viewBox="0 0 12 12"><path d="M0 2h12v8H0zM1 3l5 4 5-4" fill="none" stroke="#6c6c6c" stroke-width="1.2"/></svg>oooooo@care-tecto.jp</li>
    <li><svg viewBox="0 0 12 12"><rect x="1" y="1" width="10" height="10"/></svg>www.care-tecto.jp/blog</li>
  </ul>
</section>

<div class="side-label" style="top:534px">Back</div>
<section class="card card--back">
  <div class="back-rail">
    <div class="brand"><div class="brand-mark"></div><div class="brand-name">care tecto</div></div>
    <p class="tagline-vertical">Better Life Better Care</p>
  </div>
  <div class="back-field">
    <svg class="arc" viewBox="0 0 495 372"><path d="M30 372 C110 190 320 120 495 140" fill="none" stroke="#ffffff" stroke-width="34" opacity=".6"/></svg>
    <h1 class="place">楓庵の里</h1>
    <p class="slogan">よりよい介護で、よりよい生活を</p>
    <div class="phone-box">Tel : 0000-00-0000</div>
    <div class="service service--nursing">
      <svg class="service-shape" width="160" height="136" viewBox="0 0 160 136"><polygon points="80,0 160,136 0,136" fill="#f6d1d8"/></svg>
      <div class="service-text"><div class="service-title">訪問看護</div>訪問看護ステーション<br>「楓庵の里」</div>
    </div>
    <div class="service service--day">
      <svg class="service-shape" width="150" height="128" viewBox="0 0 150 128"><polygon points="75,0 150,128 0,128" fill="#bfe0ef"/></svg>
      <div class="service-text"><div class="service-title">デイサービス</div>「楓庵の里」</div>
    </div>
    <div class="service service--care">
      <svg class="service-shape" width="200" height="150" viewBox="0 0 200 150"><polygon points="100,0 200,150 0,150" fill="#f7e6a0"/></svg>
      <div class="service-text"><div class="service-title">居宅介護支援事業所</div>居宅介護支援センター<br>「楓庵の里」</div>
    </div>
  </div>
</section>
</body>
</html>
```